Velvet Harbor Powerpoint Presentation

Looking for powerpoint presentation template for our boutique social media management and digital marketing company.
We will be using this Powerpoint template for presentations, guest speaking sessions and proposals.
We need a front page and then a few different versions of what the rest of the template would look like.
I have attached our business cards, different versions of our logo, and our PDF so you can get a look at our identity and get a feel of what we are about. Our website will be up in about two weeks.
Target Market(s)
Small to medium size business owners (all different catagories)
Industry/Entity Type
Marketing
Requirements
Must have
- The logo
- a very boutique, high end look. You will see what I mean when you look at our business cards and our PDF.
- We only want to use the Velvet Harbor colors- Black, White, Rose Gold and Grey
Should not have
- Lot's of colors that are not part of the Velvet Harbor identity

```html
<!DOCTYPE html>
<html lang="en">
<head>
<meta charset="utf-8">
<title>Velvet Harbor – Presentation Template</title>
<link href="https://fonts.googleapis.com/css2?family=Roboto:wght@300;400;500&display=swap" rel="stylesheet">
<style>
:root{
  --ink:#1b1b1b;
  --panel:#3b3b3b;
  --grey:#7d7d7d;
  --grey-mid:#a9a9a9;
  --grey-light:#c9c9c9;
  --muted:#b4b4b4;
  --rose:#f1d6ca;
  --rose-deep:#e7b9a6;
  --paper:#ffffff;
  --canvas:#ffffff;
}
*{box-sizing:border-box;margin:0;padding:0}
html,body{width:1200px;height:1154px;overflow:hidden;background:var(--canvas)}
body{font-family:"Roboto",Arial,sans-serif;font-weight:300;color:var(--ink)}
.deck{display:grid;grid-template-columns:repeat(3,394px);grid-auto-rows:220px;column-gap:6px;row-gap:11px;padding:7px 3px;width:1200px;height:1154px}
.slide{position:relative;background:var(--paper);overflow:hidden;box-shadow:0 0 0 1px #ececec}
.slide--dark{background:var(--ink);box-shadow:none}
.slide-title{position:absolute;left:17px;top:18px;font-size:18px;font-weight:300;letter-spacing:.2px;white-space:nowrap}
.slide-title::after{content:"";position:absolute;left:0;bottom:-5px;width:26px;height:1px;background:var(--rose-deep)}
.brand{position:absolute;right:12px;top:12px;display:flex;flex-direction:column;align-items:center;gap:3px;font-size:7.5px;font-weight:300;letter-spacing:.3px;color:#444}
.brand .dot{width:11px;height:11px;border:1px solid currentColor;border-radius:50%}
.slide--dark .brand{color:#8a8a8a}
.footer{position:absolute;left:0;right:0;bottom:0;height:13px;background:var(--ink);color:#d9d9d9;font-size:4.6px;display:flex;align-items:center;justify-content:space-between;padding:0 6px 0 5px}
.footer .page{font-size:5.5px}
.lead{position:absolute;font-size:8.6px;line-height:1.4;color:#333}
.lorem{font-size:5px;line-height:1.5;color:var(--muted)}
.lorem p+p{margin-top:5px}
.heading{font-size:8.5px;color:#444;font-weight:300}
.label{font-size:6.5px;color:#333;font-weight:300}
.abs{position:absolute}
.icon{width:14px;height:14px;border-radius:50%;background:var(--ink);color:#fff;display:grid;place-items:center;flex:none}
.icon svg{width:8px;height:8px}
.icon--rose{background:var(--rose)}
.icon--grey{background:var(--grey)}
.icon--ring{background:#fff;color:var(--ink);border:1px solid var(--rose-deep)}
.icon--outline{background:transparent;border:1px solid #fff;width:26px;height:26px}
.icon--outline svg{width:12px;height:12px}
.photo{position:absolute}
.bullet{position:absolute;display:flex;gap:5px;width:100px}
.bullet .label{display:block;margin-top:1px}
.vrule{position:absolute;width:1px;background:#e6e6e6}
.hrule{position:absolute;height:1px;background:#e6e6e6}
</style>
</head>
<body>
<svg width="0" height="0" style="position:absolute" aria-hidden="true">
  <defs>
    <symbol id="i-search" viewBox="0 0 16 16"><circle cx="7" cy="7" r="4" fill="none" stroke="currentColor" stroke-width="1.8"/><line x1="10" y1="10" x2="14" y2="14" stroke="currentColor" stroke-width="2"/></symbol>
    <symbol id="i-pen" viewBox="0 0 16 16"><path d="M3 13l1-3 7-7 2 2-7 7z" fill="currentColor"/></symbol>
    <symbol id="i-gear" viewBox="0 0 16 16"><circle cx="8" cy="8" r="5" fill="none" stroke="currentColor" stroke-width="2.6" stroke-dasharray="2 1.6"/><circle cx="8" cy="8" r="2" fill="currentColor"/></symbol>
    <symbol id="i-chart" viewBox="0 0 16 16"><rect x="2" y="9" width="2.5" height="5" fill="currentColor"/><rect x="6" y="6" width="2.5" height="8" fill="currentColor"/><rect x="10" y="3" width="2.5" height="11" fill="currentColor"/></symbol>
    <symbol id="i-arrow" viewBox="0 0 16 16"><path d="M3 13L12 4M7 3.5h5.5V9" fill="none" stroke="currentColor" stroke-width="1.8"/></symbol>
    <symbol id="i-star" viewBox="0 0 16 16"><path d="M8 2l1.8 4 4.2.4-3.2 2.8 1 4.2L8 11.2 4.2 13.4l1-4.2L2 6.4 6.2 6z" fill="currentColor"/></symbol>
    <symbol id="i-users" viewBox="0 0 16 16"><circle cx="5" cy="6" r="2" fill="currentColor"/><circle cx="11" cy="6" r="2" fill="currentColor"/><path d="M1.5 13a3.5 3 0 0 1 7 0zM7.5 13a3.5 3 0 0 1 7 0z" fill="currentColor"/></symbol>
    <symbol id="i-pin" viewBox="0 0 16 16"><path d="M8 1.5a4.5 4.5 0 0 1 4.5 4.5C12.5 9.5 8 14.5 8 14.5S3.5 9.5 3.5 6A4.5 4.5 0 0 1 8 1.5z" fill="currentColor"/><circle cx="8" cy="6" r="1.6" fill="#fff"/></symbol>
    <symbol id="i-target" viewBox="0 0 16 16"><circle cx="8" cy="8" r="5.5" fill="none" stroke="currentColor" stroke-width="1.6"/><circle cx="8" cy="8" r="2.2" fill="currentColor"/></symbol>
    <symbol id="i-screen" viewBox="0 0 16 16"><rect x="2" y="3" width="12" height="8" fill="none" stroke="currentColor" stroke-width="1.6"/><rect x="6" y="12" width="4" height="1.6" fill="currentColor"/></symbol>
    <symbol id="i-cup" viewBox="0 0 16 16"><path d="M3 6h8v4a3 3 0 0 1-3 3H6a3 3 0 0 1-3-3z" fill="currentColor"/><path d="M11 7h1.5a1.5 1.5 0 0 1 0 3H11" fill="none" stroke="currentColor" stroke-width="1.2"/><path d="M5 2c0 1.5 1 1.5 1 3M8 2c0 1.5 1 1.5 1 3" fill="none" stroke="currentColor" stroke-width="1"/><rect x="2" y="14" width="11" height="1" fill="currentColor"/></symbol>
  </defs>
</svg>

<main class="deck">

  <!-- 19 -->
  <section class="slide">
    <h2 class="slide-title">OUR DIFFERENCES</h2>
    <div class="brand"><span class="dot"></span>VELVET HARBOR</div>
    <div class="abs" style="left:25px;top:66px;width:351px;height:113px;background:var(--ink)"></div>
    <div class="bullet" style="left:39px;top:82px;width:180px;align-items:center"><span class="icon icon--rose"></span><span class="lorem" style="color:#eee">Every campaign begins with a careful plan, built around the voice of your brand.</span></div>
    <div class="bullet" style="left:39px;top:105px;width:180px;align-items:center"><span class="icon icon--rose"></span><span class="lorem" style="color:#eee">We shape content that feels personal and always on message.</span></div>
    <div class="bullet" style="left:39px;top:128px;width:180px;align-items:center"><span class="icon icon--rose"></span><span class="lorem" style="color:#eee">Every campaign begins with a careful plan, built around the voice of your brand.</span></div>
    <div class="bullet" style="left:39px;top:151px;width:180px;align-items:center"><span class="icon icon--rose"></span><span class="lorem" style="color:#eee">We shape content that feels personal and always on message.</span></div>
    <div class="photo" role="img" aria-label="Photo looking up between glass towers" style="left:232px;top:81px;width:133px;height:88px;background:linear-gradient(135deg,#e9e9e9,#8f8f8f 55%,#d8d8d8)"></div>
    <footer class="footer"><span>© 2017 VELVET HARBOR. All rights reserved.</span><span class="page">19</span></footer>
  </section>

  <!-- 20 -->
  <section class="slide">
    <h2 class="slide-title">TWO COLUMN DESCRIPTION</h2>
    <div class="brand"><span class="dot"></span>VELVET HARBOR</div>
    <p class="lead" style="left:21px;top:69px;width:330px">This is place for your header text. Insert your text here, just replace this text with your own text</p>
    <div class="abs lorem" style="left:21px;top:106px;width:165px"><p>Our team builds social strategies around your goals, your audience and your story, with steady care from the first plan to the final monthly report we share.</p><p>We write, schedule and review each post so your feed stays calm, polished and true to the brand.</p></div>
    <div class="abs lorem" style="left:214px;top:106px;width:165px"><p>Our team builds social strategies around your goals, your audience and your story, with steady care from the first plan to the final monthly report we share.</p><p>We write, schedule and review each post so your feed stays calm, polished and true to the brand.</p></div>
    <footer class="footer"><span>© 2017 VELVET HARBOR. All rights reserved.</span><span class="page">20</span></footer>
  </section>

  <!-- 21 -->
  <section class="slide slide--dark">
    <div class="photo" role="img" aria-label="Dark photo of a coffee cup on a table" style="inset:0;background:radial-gradient(ellipse at 55% 75%,#2e2e2e,#121212 70%)"></div>
    <div class="brand"><span class="dot"></span>VELVET HARBOR</div>
    <svg class="abs" style="left:188px;top:118px;width:18px;height:18px;color:#fff"><use href="#i-cup"/></svg>
    <p class="abs" style="left:0;right:0;top:138px;text-align:center;color:#fff;font-size:13px;letter-spacing:.3px">COFFEE BREAK</p>
    <p class="abs" style="left:0;right:0;top:156px;text-align:center;color:#ddd;font-size:6.5px">Back in 15 minutes</p>
  </section>

  <!-- 22 -->
  <section class="slide">
    <h2 class="slide-title">THREE COLUMN DESCRIPTION</h2>
    <div class="brand"><span class="dot"></span>VELVET HARBOR</div>
    <p class="lead" style="left:21px;top:54px;width:350px">This is place for your header text. Insert your text here, just replace this text with your own text</p>
    <div class="abs lorem" style="left:21px;top:89px;width:100px"><p>We plan content calendars with care, match each post to your brand voice, and keep your audience engaged through every season of the year.</p><p>Gentle growth, honest results and clear monthly notes.</p></div>
    <div class="vrule" style="left:134px;top:90px;height:95px"></div>
    <div class="abs lorem" style="left:147px;top:89px;width:100px"><p>We plan content calendars with care, match each post to your brand voice, and keep your audience engaged through every season of the year.</p><p>Gentle growth, honest results and clear monthly notes.</p></div>
    <div class="vrule" style="left:260px;top:90px;height:95px"></div>
    <div class="abs lorem" style="left:272px;top:86px;width:100px"><p>We plan content calendars with care, match each post to your brand voice, and keep your audience engaged through every season of the year.</p><p>Gentle growth, honest results and clear monthly notes.</p></div>
    <footer class="footer"><span>© 2017 VELVET HARBOR. All rights reserved.</span><span class="page">22</span></footer>
  </section>

  <!-- 23 -->
  <section class="slide">
    <div class="photo" role="img" aria-label="Black and white photo of a checkered building facade" style="left:0;top:0;width:234px;height:220px;background:linear-gradient(120deg,#cfcfcf,#6b6b6b 45%,#e6e6e6 70%,#4a4a4a)"></div>
    <div class="abs" style="left:234px;top:0;width:160px;height:220px;background:var(--panel)"></div>
    <div class="abs" style="left:234px;top:18px;width:160px;display:flex;flex-direction:column;align-items:center;gap:5px;color:#d0d0d0"><span style="width:20px;height:20px;border:1px solid var(--rose-deep);border-radius:50%"></span><span style="font-size:11px;letter-spacing:.4px">VELVET HARBOR</span></div>
    <div class="abs" style="left:250px;top:76px;display:flex;gap:17px;color:#fff">
      <span class="icon icon--outline"><svg><use href="#i-arrow"/></svg></span>
      <span class="icon icon--outline"><svg><use href="#i-target"/></svg></span>
      <span class="icon icon--outline"><svg><use href="#i-star"/></svg></span>
    </div>
    <p class="abs" style="left:250px;top:121px;color:#fff;font-size:14.5px;line-height:1.1">YOUR TITLE<br>GOES HERE</p>
    <p class="abs lorem" style="left:250px;top:157px;width:110px;color:#e6e6e6">Calm, considered social media for small brands that want to be seen and remembered.</p>
    <div class="abs" style="left:243px;top:201px;width:142px;height:19px;background:var(--rose);font-size:5.8px;color:#555;display:grid;place-items:center">www.velvetharbor.co</div>
  </section>

  <!-- 24 -->
  <section class="slide">
    <h2 class="slide-title">YOUR TITLE GOES HERE</h2>
    <div class="brand"><span class="dot"></span>VELVET HARBOR</div>
    <p class="abs heading" style="left:17px;top:47px;font-size:7.5px">Heading Goes Here</p>
    <p class="abs lorem" style="left:17px;top:57px;width:362px">Each plan is written around your audience, your goals and your voice, so every post and every story feels like it truly belongs to your brand and your clients.</p>
    <div class="bullet" style="left:17px;top:84px;width:170px"><span class="icon"><svg><use href="#i-chart"/></svg></span><span><span class="label">Service Number One</span><span class="lorem" style="display:block">Short note on this service and the value it brings to your brand each month.</span></span></div>
    <div class="bullet" style="left:17px;top:118px;width:170px"><span class="icon icon--rose"><svg><use href="#i-arrow"/></svg></span><span><span class="label" style="color:var(--rose-deep)">Service Number Two</span><span class="lorem" style="display:block">Short note on this service and the value it brings to your brand each month.</span></span></div>
    <div class="bullet" style="left:17px;top:157px;width:170px"><span class="icon icon--grey"><svg><use href="#i-search"/></svg></span><span><span class="label">Service Number Three</span><span class="lorem" style="display:block">Short note on this service and the value it brings to your brand each month.</span></span></div>
    <div class="abs" style="left:206px;top:79px;width:171px;height:31px;background:var(--ink);color:#fff;display:flex;align-items:center;gap:6px;padding-left:8px"><span style="font-size:18px;font-weight:400">1</span><span style="width:1px;height:18px;background:#fff"></span><span class="lorem" style="color:#fff;width:125px">A short line about this first step and the results it brings for you.</span></div>
    <div class="abs" style="left:206px;top:116px;width:171px;height:32px;background:var(--rose);color:var(--grey);display:flex;align-items:center;gap:6px;padding-left:8px"><span style="font-size:18px;font-weight:400">2</span><span style="width:1px;height:18px;background:var(--grey)"></span><span class="lorem" style="color:var(--grey);width:125px">A short line about this second step and the results it brings for you.</span></div>
    <div class="abs" style="left:206px;top:153px;width:171px;height:31px;background:var(--grey);color:#fff;display:flex;align-items:center;gap:6px;padding-left:8px"><span style="font-size:18px;font-weight:400">3</span><span style="width:1px;height:18px;background:#fff"></span><span class="lorem" style="color:#fff;width:125px">A short line about this third step and the results it brings for you.</span></div>
    <footer class="footer"><span>© 2017 VELVET HARBOR. All rights reserved.</span><span class="page">24</span></footer>
  </section>

  <!-- 25 -->
  <section class="slide">
    <h2 class="slide-title">FOUR BULLETS WITH PARAGRAPH</h2>
    <div class="brand"><span class="dot"></span>VELVET HARBOR</div>
    <div class="bullet" style="left:24px;top:72px;width:80px"><span class="icon"><svg><use href="#i-search"/></svg></span><span><span class="label">Your Text Here</span><span class="lorem" style="display:block">Brief note on this point, kept short and clear.</span></span></div>
    <div class="bullet" style="left:112px;top:72px;width:80px"><span class="icon"><svg><use href="#i-pen"/></svg></span><span><span class="label">Your Text Here</span><span class="lorem" style="display:block">Brief note on this point, kept short and clear.</span></span></div>
    <div class="bullet" style="left:24px;top:136px;width:80px"><span class="icon"><svg><use href="#i-gear"/></svg></span><span><span class="label">Your Text Here</span><span class="lorem" style="display:block">Brief note on this point, kept short and clear.</span></span></div>
    <div class="bullet" style="left:112px;top:136px;width:80px"><span class="icon"><svg><use href="#i-arrow"/></svg></span><span><span class="label">Your Text Here</span><span class="lorem" style="display:block">Brief note on this point, kept short and clear.</span></span></div>
    <p class="abs heading" style="left:216px;top:71px">Heading Goes Here</p>
    <div class="abs lorem" style="left:216px;top:84px;width:162px"><p>Every brand has a story worth telling. We help you share it with care, grace and a steady rhythm online.</p><p>Clear plans, honest numbers and monthly reviews keep us aligned.</p><p>We listen first, then build a voice your clients will trust and return to.</p></div>
    <footer class="footer"><span>© 2017 VELVET HARBOR. All rights reserved.</span><span class="page">25</span></footer>
  </section>

  <!-- 26 -->
  <section class="slide">
    <h2 class="slide-title">YOUR TITLE</h2>
    <div class="brand"><span class="dot"></span>VELVET HARBOR</div>
    <div class="photo" role="img" aria-label="Photo of an angular building facade" style="left:125px;top:0;width:143px;height:207px;background:linear-gradient(160deg,#f1f1f1,#9a9a9a 40%,#dedede 65%,#5c5c5c)"></div>
    <p class="abs heading" style="left:16px;top:65px">Heading Goes Here</p>
    <div class="abs lorem" style="left:16px;top:78px;width:102px"><p>We craft thoughtful content and calm campaigns for brands that value quality.</p><p>Each month we review, refine and report back clearly.</p><p>Your audience grows with care, one post at a time.</p></div>
    <div class="bullet" style="left:282px;top:67px"><span class="icon"><svg><use href="#i-search"/></svg></span><span><span class="label">Your Text Here</span><span class="lorem" style="display:block">Short note, kept brief and clear.</span></span></div>
    <div class="bullet" style="left:282px;top:99px"><span class="icon"><svg><use href="#i-pen"/></svg></span><span><span class="label">Your Text Here</span><span class="lorem" style="display:block">Short note, kept brief and clear.</span></span></div>
    <div class="bullet" style="left:282px;top:130px"><span class="icon"><svg><use href="#i-arrow"/></svg></span><span><span class="label">Your Text Here</span><span class="lorem" style="display:block">Short note, kept brief and clear.</span></span></div>
    <div class="bullet" style="left:282px;top:163px"><span class="icon"><svg><use href="#i-gear"/></svg></span><span><span class="label">Your Text Here</span><span class="lorem" style="display:block">Short note, kept brief and clear.</span></span></div>
    <footer class="footer"><span>© 2017 VELVET HARBOR. All rights reserved.</span><span class="page">26</span></footer>
  </section>

  <!-- 27 -->
  <section class="slide">
    <h2 class="slide-title">TEXT &amp; BULLET AREA</h2>
    <div class="brand"><span class="dot"></span>VELVET HARBOR</div>
    <p class="abs heading" style="left:20px;top:62px">Heading Goes Here</p>
    <div class="abs lorem" style="left:20px;top:76px;width:103px"><p>We craft thoughtful content and calm campaigns for brands that value quality.</p><p>Each month we review, refine and report back clearly to you.</p><p>Your audience grows with care, one post at a time.</p></div>
    <div class="bullet" style="left:153px;top:62px"><span class="icon"><svg><use href="#i-star"/></svg></span><span><span class="label">Your Text Here</span><span class="lorem" style="display:block">Short note, kept brief and clear.</span></span></div>
    <div class="bullet" style="left:153px;top:95px"><span class="icon"><svg><use href="#i-chart"/></svg></span><span><span class="label">Your Text Here</span><span class="lorem" style="display:block">Short note, kept brief and clear.</span></span></div>
    <div class="bullet" style="left:153px;top:127px"><span class="icon"><svg><use href="#i-users"/></svg></span><span><span class="label">Your Text Here</span><span class="lorem" style="display:block">Short note, kept brief and clear.</span></span></div>
    <div class="bullet" style="left:153px;top:159px"><span class="icon"><svg><use href="#i-target"/></svg></span><span><span class="label">Your Text Here</span><span class="lorem" style="display:block">Short note, kept brief and clear.</span></span></div>
    <div class="bullet" style="left:277px;top:62px"><span class="icon"><svg><use href="#i-search"/></svg></span><span><span class="label">Your Text Here</span><span class="lorem" style="display:block">Short note, kept brief and clear.</span></span></div>
    <div class="bullet" style="left:277px;top:95px"><span class="icon"><svg><use href="#i-pen"/></svg></span><span><span class="label">Your Text Here</span><span class="lorem" style="display:block">Short note, kept brief and clear.</span></span></div>
    <div class="bullet" style="left:277px;top:127px"><span class="icon"><svg><use href="#i-arrow"/></svg></span><span><span class="label">Your Text Here</span><span class="lorem" style="display:block">Short note, kept brief and clear.</span></span></div>
    <div class="bullet" style="left:277px;top:159px"><span class="icon"><svg><use href="#i-gear"/></svg></span><span><span class="label">Your Text Here</span><span class="lorem" style="display:block">Short note, kept brief and clear.</span></span></div>
    <footer class="footer"><span>© 2017 VELVET HARBOR. All rights reserved.</span><span class="page">27</span></footer>
  </section>

  <!-- 28 -->
  <section class="slide slide--dark">
    <span class="abs" style="left:185px;top:52px;width:24px;height:24px;border:1px solid var(--rose-deep);border-radius:50%"></span>
    <p class="abs" style="left:0;right:0;top:86px;text-align:center;color:#9a9a9a;font-size:16px;letter-spacing:.5px">VELVET HARBOR</p>
    <p class="abs" style="left:0;right:0;top:152px;text-align:center;color:#ddd;font-size:6.5px">Divider Page</p>
    <p class="abs" style="left:0;right:0;top:161px;text-align:center;color:#fff;font-size:17px">YOUR TITLE GOES HERE</p>
    <p class="abs" style="left:0;right:0;top:183px;text-align:center;color:#ddd;font-size:8.5px">Your Subtitle Here</p>
  </section>

  <!-- 29 -->
  <section class="slide">
    <h2 class="slide-title">PARAGRAPH WITH THREE BULLET</h2>
    <div class="brand"><span class="dot"></span>VELVET HARBOR</div>
    <p class="lead" style="left:18px;top:56px;width:330px">This is place for your header text. Insert your text here, just replace this text with your own text</p>
    <div class="abs lorem" style="left:21px;top:97px;width:103px"><p>We craft thoughtful content and calm campaigns for brands that value quality and lasting trust with their clients online.</p><p>Each month we review, refine and report back clearly to you.</p></div>
    <div class="vrule" style="left:140px;top:92px;height:90px"></div>
    <div class="abs" style="left:150px;top:92px;width:236px;display:grid;grid-template-columns:repeat(3,1fr);column-gap:8px;text-align:center">
      <div><span class="icon icon--ring" style="margin:0 auto"><svg><use href="#i-target"/></svg></span><p class="label" style="margin-top:10px">Your Text Here</p><p class="lorem">Short note on this point, kept brief and clear for all.</p><p class="lorem" style="margin-top:5px">A second short line of support text here.</p></div>
      <div><span class="icon icon--ring" style="margin:0 auto"><svg><use href="#i-star"/></svg></span><p class="label" style="margin-top:10px">Your Text Here</p><p class="lorem">Short note on this point, kept brief and clear for all.</p><p class="lorem" style="margin-top:5px">A second short line of support text here.</p></div>
      <div><span class="icon icon--ring" style="margin:0 auto"><svg><use href="#i-arrow"/></svg></span><p class="label" style="margin-top:10px">Your Text Here</p><p class="lorem">Short note on this point, kept brief and clear for all.</p><p class="lorem" style="margin-top:5px">A second short line of support text here.</p></div>
    </div>
    <footer class="footer"><span>© 2017 VELVET HARBOR. All rights reserved.</span><span class="page">29</span></footer>
  </section>

  <!-- 30 -->
  <section class="slide">
    <h2 class="slide-title">GLOBAL EXPERIENCE</h2>
    <div class="brand"><span class="dot"></span>VELVET HARBOR</div>
    <div class="photo" role="img" aria-label="Grey world map with client locations marked" style="left:98px;top:40px;width:284px;height:123px;border-radius:40px;background:radial-gradient(ellipse at 50% 50%,#cfcfcf,#e8e8e8 70%,#fff)"></div>
    <span class="abs" style="left:17px;top:169px;width:13px;height:13px;border-radius:50%;background:var(--ink)"></span>
    <p class="abs heading" style="left:37px;top:171px;font-size:7.5px">Heading Goes Here</p>
    <p class="abs lorem" style="left:17px;top:184px;width:210px">We support brands across many regions, with the same calm care and clear results for each.</p>
    <footer class="footer"><span>© 2017 VELVET HARBOR. All rights reserved.</span><span class="page">30</span></footer>
  </section>

  <!-- 31 -->
  <section class="slide">
    <h2 class="slide-title">MULTIPLE COLUMN AREA</h2>
    <div class="brand"><span class="dot"></span>VELVET HARBOR</div>
    <div class="abs" style="left:14px;top:60px;width:362px;display:grid;grid-template-columns:repeat(5,1fr);text-align:center">
      <div><span class="icon" style="margin:0 auto"><svg><use href="#i-gear"/></svg></span><p class="label" style="margin-top:3px">Your Text Here</p><p class="lorem">Short note kept<br>brief here.</p></div>
      <div><span class="icon" style="margin:0 auto"><svg><use href="#i-arrow"/></svg></span><p class="label" style="margin-top:3px">Your Text Here</p><p class="lorem">Short note kept<br>brief here.</p></div>
      <div><span class="icon" style="margin:0 auto"><svg><use href="#i-search"/></svg></span><p class="label" style="margin-top:3px">Your Text Here</p><p class="lorem">Short note kept<br>brief here.</p></div>
      <div><span class="icon" style="margin:0 auto"><svg><use href="#i-pen"/></svg></span><p class="label" style="margin-top:3px">Your Text Here</p><p class="lorem">Short note kept<br>brief here.</p></div>
      <div><span class="icon" style="margin:0 auto"><svg><use href="#i-chart"/></svg></span><p class="label" style="margin-top:3px">Your Text Here</p><p class="lorem">Short note kept<br>brief here.</p></div>
    </div>
    <div class="hrule" style="left:28px;top:117px;width:340px"></div>
    <p class="abs heading" style="left:28px;top:136px">Heading Goes Here</p>
    <div class="abs lorem" style="left:28px;top:148px;width:160px"><p>We craft thoughtful content and calm campaigns for brands that value quality and lasting trust.</p><p>Each month we review, refine and report back clearly.</p></div>
    <p class="abs heading" style="left:212px;top:136px">Heading Goes Here</p>
    <div class="abs lorem" style="left:212px;top:148px;width:160px"><p>We craft thoughtful content and calm campaigns for brands that value quality and lasting trust.</p><p>Each month we review, refine and report back clearly.</p></div>
    <footer class="footer"><span>© 2017 VELVET HARBOR. All rights reserved.</span><span class="page">31</span></footer>
  </section>

  <!-- 32 -->
  <section class="slide">
    <h2 class="slide-title">YOUR PIE CHART AREA</h2>
    <div class="brand"><span class="dot"></span>VELVET HARBOR</div>
    <svg class="abs" style="left:0;top:76px" width="394" height="46" viewBox="0 0 394 46" role="img" aria-label="Four donut charts: 20, 50, 70 and 30 percent">
      <g fill="none" stroke-width="5">
        <circle cx="58" cy="23" r="19" stroke="#d6d6d6"/>
        <circle cx="58" cy="23" r="19" stroke="#1b1b1b" stroke-dasharray="23.9 119.4" transform="rotate(-90 58 23)"/>
        <circle cx="146" cy="23" r="19" stroke="#f7ebe5"/>
        <circle cx="146" cy="23" r="19" stroke="#f1d6ca" stroke-dasharray="59.7 119.4" transform="rotate(-90 146 23)"/>
        <circle cx="236" cy="23" r="19" stroke="#d6d6d6"/>
        <circle cx="236" cy="23" r="19" stroke="#555" stroke-dasharray="83.6 119.4" transform="rotate(-90 236 23)"/>
        <circle cx="330" cy="23" r="19" stroke="#e3e3e3"/>
        <circle cx="330" cy="23" r="19" stroke="#a9a9a9" stroke-dasharray="35.8 119.4" transform="rotate(-90 330 23)"/>
      </g>
      <g font-family="Roboto, Arial, sans-serif" font-weight="300" font-size="11" text-anchor="middle">
        <text x="58" y="27" fill="#1b1b1b">20%</text>
        <text x="146" y="27" fill="#f1d6ca">50%</text>
        <text x="236" y="27" fill="#555">70%</text>
        <text x="330" y="27" fill="#a9a9a9">30%</text>
      </g>
    </svg>
    <div class="abs" style="left:18px;top:131px;width:358px;display:grid;grid-template-columns:repeat(4,1fr);column-gap:14px;text-align:center">
      <div><p class="lorem" style="color:#333;font-weight:400">Subtitle in this area</p><p class="lorem">A short note about this figure and what it shows for the brand.</p></div>
      <div><p class="lorem" style="color:var(--rose-deep)">Subtitle in this area</p><p class="lorem">A short note about this figure and what it shows for the brand.</p></div>
      <div><p class="lorem" style="color:#333;font-weight:400">Subtitle in this area</p><p class="lorem">A short note about this figure and what it shows for the brand.</p></div>
      <div><p class="lorem" style="color:#555">Subtitle in this area</p><p class="lorem">A short note about this figure and what it shows for the brand.</p></div>
    </div>
    <footer class="footer"><span>© 2017 VELVET HARBOR. All rights reserved.</span><span class="page">32</span></footer>
  </section>

  <!-- 33 -->
  <section class="slide">
    <h2 class="slide-title">YOUR PIE CHART AREA</h2>
    <div class="brand"><span class="dot"></span>VELVET HARBOR</div>
    <svg class="abs" style="left:152px;top:70px" width="90" height="90" viewBox="0 0 90 90" role="img" aria-label="Donut chart split into four shares">
      <g fill="none" stroke-width="24">
        <circle cx="45" cy="45" r="31" stroke="#f1d6ca" stroke-dasharray="68 194.8" transform="rotate(-90 45 45)"/>
        <circle cx="45" cy="45" r="31" stroke="#7d7d7d" stroke-dasharray="48.7 194.8" stroke-dashoffset="-68" transform="rotate(-90 45 45)"/>
        <circle cx="45" cy="45" r="31" stroke="#a9a9a9" stroke-dasharray="39 194.8" stroke-dashoffset="-116.7" transform="rotate(-90 45 45)"/>
        <circle cx="45" cy="45" r="31" stroke="#1b1b1b" stroke-dasharray="39.1 194.8" stroke-dashoffset="-155.7" transform="rotate(-90 45 45)"/>
      </g>
      <g font-family="Roboto, Arial, sans-serif" font-weight="500" font-size="7.5" text-anchor="middle">
        <text x="24" y="27" fill="#fff">20%</text>
        <text x="74" y="42" fill="#b08a7a">35%</text>
        <text x="58" y="78" fill="#fff">40%</text>
        <text x="16" y="70" fill="#fff">30%</text>
      </g>
    </svg>
    <div class="abs" style="left:58px;top:63px;width:68px;text-align:right"><p class="lorem" style="color:#333;font-weight:400">Secure</p><p class="lorem">Short note here,<br>kept very brief.</p></div>
    <span class="icon abs" style="left:132px;top:66px;width:22px;height:22px"><svg style="width:12px;height:12px"><use href="#i-target"/></svg></span>
    <div class="abs" style="left:38px;top:138px;width:68px;text-align:right"><p class="lorem" style="color:#333;font-weight:400">Good Package</p><p class="lorem">Short note here,<br>kept very brief.</p></div>
    <span class="icon icon--grey abs" style="left:112px;top:140px;width:22px;height:22px;background:var(--grey-light)"><svg style="width:12px;height:12px"><use href="#i-pin"/></svg></span>
    <span class="icon icon--rose abs" style="left:264px;top:69px;width:22px;height:22px"><svg style="width:12px;height:12px"><use href="#i-arrow"/></svg></span>
    <div class="abs" style="left:291px;top:66px;width:68px"><p class="lorem" style="color:var(--rose-deep)">Well Organized</p><p class="lorem">Short note here,<br>kept very brief.</p></div>
    <span class="icon icon--grey abs" style="left:266px;top:139px;width:22px;height:22px"><svg style="width:12px;height:12px"><use href="#i-screen"/></svg></span>
    <div class="abs" style="left:293px;top:136px;width:68px"><p class="lorem" style="color:#333;font-weight:400">Publication</p><p class="lorem">Short note here,<br>kept very brief.</p></div>
    <p class="abs lorem" style="left:60px;top:178px;width:274px;text-align:center">Every figure here reflects a real plan, a clear goal and steady work on content, timing and audience care across each channel we manage.</p>
    <footer class="footer"><span>© 2017 VELVET HARBOR. All rights reserved.</span><span class="page">33</span></footer>
  </section>

</main>
</body>
</html>
```